Business Card, Letterhead, Envelopes, Thank you cards, Post Cards
Business cards and stationary for life coach
Professional
Silver Heron Guidance Studio
Marla Penrick, MA
4810 North Calloway Avenue
Suite C 240
Missoula, Montana 59417
silverheronguidance@mailbox-example.net
silverheronguidance-example.com
I would like to see 'Let Your Dreams Take Flight' on the front of the card. This is the tagline. Please use a compatible font with the logo.
'Dragonfly spends most of her life underwater until the day she discovers her wings and soars upon the wind.' I'd like to see this in script, similar to the logo font.
Please let me know if you need different files.

```html
<!DOCTYPE html>
<html lang="en">
<head>
<meta charset="utf-8">
<title>Silver Heron Guidance Studio – Business Card</title>
<link rel="stylesheet" href="https://fonts.googleapis.com/css2?family=Open+Sans:ital,wght@0,400;0,600;0,700;1,400&display=swap">
<style>
  :root {
    --page-bg: #e9e4dc;
    --label-ink: #1a1a1a;
    --brand-blue: #1f6fc9;
    --deep-blue: #1552b0;
    --sky-blue: #3fa6ec;
    --light-blue: #8fd0f6;
    --card-white: #ffffff;
    --body-ink: #2b2b2b;
  }
  * { box-sizing: border-box; margin: 0; padding: 0; }
  html, body { width: 1200px; height: 799px; overflow: hidden; }
  body {
    background: var(--page-bg);
    font-family: "Open Sans", Arial, sans-serif;
    position: relative;
  }
  .card-label {
    position: absolute;
    top: 220px;
    width: 476px;
    text-align: center;
    font-weight: 700;
    font-size: 24px;
    line-height: 30px;
    color: var(--label-ink);
  }
  .card-label--front { left: 100px; }
  .card-label--back { left: 631px; }

  .card {
    position: absolute;
    top: 269px;
    width: 476px;
    height: 331px;
    border-radius: 18px;
    overflow: hidden;
    box-shadow: 0 3px 8px rgba(0,0,0,0.25);
  }
  .card--front { left: 100px; background: var(--card-white); }
  .card--back {
    left: 631px;
    background: linear-gradient(180deg, var(--deep-blue) 0%, var(--brand-blue) 45%, var(--sky-blue) 100%);
    color: var(--card-white);
  }
  .card__swoosh { position: absolute; inset: 0; }

  .brand {
    position: absolute;
    color: var(--brand-blue);
  }
  .brand-name {
    display: flex;
    align-items: center;
    gap: 8px;
    font-weight: 600;
  }
  .brand-name__dot {
    width: 12px; height: 12px; border-radius: 50%;
    background: var(--brand-blue);
    flex: none;
  }
  .card--front .brand {
    left: 30px; top: 52px; width: 190px;
  }
  .card--front .brand-name { font-size: 16px; line-height: 20px; }
  .tagline {
    margin-top: 6px;
    padding-left: 20px;
    font-size: 10px;
    line-height: 13px;
    letter-spacing: 0.4px;
    color: var(--brand-blue);
  }
  .holder-name {
    position: absolute;
    left: 292px; top: 62px;
    font-size: 16px;
    line-height: 20px;
    color: var(--brand-blue);
    white-space: nowrap;
  }
  .contact {
    position: absolute;
    left: 30px; top: 172px;
    font-size: 11px;
    line-height: 15px;
    color: var(--body-ink);
    list-style: none;
  }
  .contact__row { display: flex; align-items: center; gap: 6px; }
  .contact__row svg { flex: none; }
  .contact__address { margin-bottom: 8px; }

  .card--back .brand {
    left: 0; right: 0; top: 120px;
    color: var(--card-white);
  }
  .card--back .brand-name {
    justify-content: center;
    font-size: 20px;
    line-height: 26px;
  }
  .card--back .brand-name__dot { background: var(--card-white); }
  .quote {
    position: absolute;
    left: 40px; right: 40px; top: 196px;
    text-align: center;
    font-style: italic;
    font-size: 11px;
    line-height: 15px;
  }
</style>
</head>
<body>
  <h2 class="card-label card-label--front">Business Card (Front)</h2>
  <h2 class="card-label card-label--back">Business Card (Back)</h2>

  <section class="card card--front">
    <svg class="card__swoosh" width="476" height="331" viewBox="0 0 476 331" aria-hidden="true">
      <defs>
        <linearGradient id="swooshBlue" x1="0" y1="0" x2="0" y2="1">
          <stop offset="0" stop-color="#1552b0"/>
          <stop offset="1" stop-color="#3fa6ec"/>
        </linearGradient>
      </defs>
      <path d="M410 0 C470 80 476 210 420 331 L476 331 L476 0 Z" fill="url(#swooshBlue)"/>
      <path d="M418 0 C468 90 468 220 408 331" fill="none" stroke="#ffffff" stroke-width="3"/>
      <path d="M400 0 C452 90 458 220 400 331" fill="none" stroke="#8fd0f6" stroke-width="1.5"/>
    </svg>
    <div class="brand">
      <div class="brand-name"><span class="brand-name__dot"></span>Silver Heron Guidance Studio</div>
      <p class="tagline">Let Your Dreams Take Flight</p>
    </div>
    <p class="holder-name">Marla Penrick, MA</p>
    <ul class="contact">
      <li class="contact__address">4810 North Calloway Avenue<br>Suite C 240, Missoula, Montana 59417</li>
      <li class="contact__row">
        <svg width="9" height="9" viewBox="0 0 10 10" aria-hidden="true"><path d="M2 1 L4 1 L5 3 L4 4 Q5 6 6 6 L7 5 L9 6 L9 8 Q8 9 7 9 Q1 8 1 2 Q1 1 2 1Z" fill="#1f6fc9"/></svg>
        406-555-0147</li>
      <li class="contact__row">
        <svg width="9" height="9" viewBox="0 0 10 10" aria-hidden="true"><rect x="0.5" y="2" width="9" height="6" fill="none" stroke="#1f6fc9"/><path d="M0.5 2 L5 5.5 L9.5 2" fill="none" stroke="#1f6fc9"/></svg>
        silverheronguidance@mailbox-example.net</li>
      <li class="contact__row">
        <svg width="9" height="9" viewBox="0 0 10 10" aria-hidden="true"><circle cx="5" cy="5" r="4.5" fill="#1f6fc9"/></svg>
        silverheronguidance-example.com</li>
    </ul>
  </section>

  <section class="card card--back">
    <div class="brand">
      <div class="brand-name"><span class="brand-name__dot"></span>Silver Heron Guidance Studio</div>
    </div>
    <p class="quote">'Dragonfly spends most of her life underwater<br>until the day she discovers her wings<br>and soars upon the wind.'</p>
  </section>
</body>
</html>
```